I need a business card designed using the logo provided either vertical or horizontal......Crestmoor Property Partners is an Australian based real estate company that caters for the upper end of the market so the design of the business card "must reflect" the companies image!!
Colour combinations are optional but "must be realistic" and must be able to be accurately useable CMYK colours.
Please consider that any colours used "must be able to be used" and be suitable in following designs for "pull out banner signs" and "real estate signs".
The colours and the font in the attached designs are for example and other combinations are encouraged.
Target Market(s)
The High End of the Australian real estate market
Industry/Entity Type
Business
Contact Information for Business Card
Logo - Business Name - Director + Licensed Real Estate Agent - Mobile Number (Cell Phone) - Business Number - Fax - Email Address - Web address
Requirements
Must have
- Designs and colours (CMYK) that can easily be interpreted by an Australian printer.
Nice to have
- Some alternative ideas on colour and font..........the ones provided are ok and have been provided as an example but I am looking for alternative ideas
Should not have
- Loud, overly bright colours. Designs that do not reflect the professional standards of the business.
- Designs that look good on a computer monitor but can not be re-created on a printing press.............this is most important when it comes to shading etc.

```html
<!DOCTYPE html>
<html lang="en">
<head>
<meta charset="utf-8">
<title>Crestmoor Property Partners – Business Card</title>
<link href="https://fonts.googleapis.com/css2?family=Michroma&family=Open+Sans:wght@400;600&display=swap" rel="stylesheet">
<style>
  :root {
    --page: #e9e9e9;
    --card: #f4f4f4;
    --maroon: #7a1e2c;
    --wine: #3a0f17;
    --gold: #b8892f;
    --ink: #3c3c3c;
    --grey-text: #5a5a5a;
    --skyline: #d6d6d6;
    --wave-edge: #d9d9d9;
  }
  * { box-sizing: border-box; margin: 0; padding: 0; }
  html, body { width: 1200px; height: 1192px; overflow: hidden; }
  body {
    background: var(--page);
    font-family: "Open Sans", sans-serif;
    display: flex;
    flex-direction: column;
    align-items: center;
    justify-content: center;
    gap: 56px;
  }
  .card {
    position: relative;
    width: 880px;
    height: 503px;
    background: var(--card);
    overflow: hidden;
    box-shadow: 0 6px 18px rgba(0,0,0,0.12);
  }
  /* Front */
  .front .swoosh { position: absolute; left: 0; top: 0; width: 880px; height: 503px; }
  .front .contact {
    position: absolute;
    left: 70px;
    top: 36px;
    z-index: 1;
  }
  .front .name {
    font-family: "Michroma", sans-serif;
    font-size: 22px;
    line-height: 34px;
    letter-spacing: 5px;
    color: var(--ink);
    text-transform: uppercase;
  }
  .front .role {
    font-family: "Michroma", sans-serif;
    font-size: 13px;
    line-height: 18px;
    letter-spacing: 2px;
    color: var(--maroon);
    margin-top: 8px;
  }
  .front .company {
    font-family: "Michroma", sans-serif;
    font-size: 13px;
    line-height: 18px;
    letter-spacing: 2px;
    color: var(--maroon);
    margin-top: 16px;
  }
  .front .details {
    list-style: none;
    margin-top: 8px;
    font-size: 16px;
    color: var(--grey-text);
    line-height: 25px;
  }
  .front .details li { display: flex; align-items: center; gap: 14px; }
  .front .details .icon { width: 16px; height: 16px; flex: none; }
  .front .details .plain { padding-left: 30px; }
  .brand {
    font-family: "Open Sans", sans-serif;
    font-weight: 600;
    color: var(--maroon);
    display: flex;
    align-items: center;
    gap: 12px;
    text-transform: uppercase;
    letter-spacing: 2px;
  }
  .brand .mark { width: 22px; height: 22px; background: var(--maroon); flex: none; }
  .front .brand {
    position: absolute;
    right: 60px;
    top: 170px;
    font-size: 18px;
    width: 270px;
    line-height: 1.3;
  }
  /* Back */
  .back .skyline {
    position: absolute;
    left: 60px;
    right: 140px;
    top: 60px;
    bottom: 40px;
    background: linear-gradient(180deg, #e4e4e4 0%, var(--skyline) 100%);
    opacity: 0.8;
  }
  .back .brand {
    position: absolute;
    left: 50%;
    top: 50%;
    transform: translate(-50%, -50%);
    font-size: 26px;
    white-space: nowrap;
  }
</style>
</head>
<body>
  <section class="card front" aria-label="Business card front">
    <svg class="swoosh" viewBox="0 0 880 503" aria-hidden="true">
      <path d="M0 284 C 150 304, 300 424, 560 456 C 720 474, 820 478, 880 478 L880 503 L0 503 Z" fill="var(--wave-edge)"/>
      <path d="M0 296 C 150 318, 300 436, 560 468 C 720 486, 820 490, 880 490 L880 503 L0 503 Z" fill="var(--gold)"/>
      <path d="M0 305 C 150 330, 300 447, 560 478 C 720 496, 820 500, 880 500 L880 503 L0 503 Z" fill="var(--wine)"/>
    </svg>
    <div class="contact">
      <p class="name">Elliot Marsh</p>
      <p class="role">CEO</p>
      <p class="company">Crestmoor Property Partners</p>
      <ul class="details">
        <li class="plain">18 Harbour Lane, Toorak, Melbourne.</li>
        <li>
          <svg class="icon" viewBox="0 0 16 16"><rect x="4" y="1" width="8" height="14" rx="1.5" fill="none" stroke="#7a1e2c" stroke-width="1.6"/><circle cx="8" cy="12.3" r="0.9" fill="#7a1e2c"/></svg>
          +61 412 555 019
        </li>
        <li>
          <svg class="icon" viewBox="0 0 16 16"><path d="M3 2h3l1 3-2 1.5a9 9 0 0 0 4.5 4.5L11 9l3 1v3a1.5 1.5 0 0 1-1.5 1.5A11.5 11.5 0 0 1 1.5 3.5 1.5 1.5 0 0 1 3 2z" fill="#7a1e2c"/></svg>
          +61 3 9555 0142
        </li>
        <li>
          <svg class="icon" viewBox="0 0 16 16"><rect x="1" y="3" width="14" height="10" rx="1" fill="none" stroke="#7a1e2c" stroke-width="1.6"/><path d="M1.5 3.5 8 9l6.5-5.5" fill="none" stroke="#7a1e2c" stroke-width="1.6"/></svg>
          elliot@crestmoorproperty.com
        </li>
        <li>
          <svg class="icon" viewBox="0 0 16 16"><circle cx="8" cy="8" r="6.8" fill="none" stroke="#7a1e2c" stroke-width="1.5"/><ellipse cx="8" cy="8" rx="3" ry="6.8" fill="none" stroke="#7a1e2c" stroke-width="1.2"/><path d="M1.2 8h13.6" stroke="#7a1e2c" stroke-width="1.2"/></svg>
          www.crestmoorproperty.com
        </li>
      </ul>
    </div>
    <div class="brand"><span class="mark"></span><span>Crestmoor Property Partners</span></div>
  </section>

  <section class="card back" aria-label="Business card back">
    <div class="skyline" role="img" aria-label="Faint grey city skyline silhouette"></div>
    <div class="brand"><span class="mark"></span><span>Crestmoor Property Partners</span></div>
  </section>
</body>
</html>
```